RM Cargoline businesscard project

RM Cargoline Ltd is a freshly founded small (3 employees), young (average age is 30 years) company, living from the road transportation market without own tools.
We would like to have an impressive, new-line, cool busines card for a freshly founded forwarding company on an overcrowded market which raises attention and makes the potential partners eager to work with us.

Target Market(s)

The main profile of the company is logistic/forwarding on road.

Industry/Entity Type

Freight Forwarding

Contact Information for Business Card

Name: Berki Zsófia
Title: general manager
mobile nr: +36-70/482-5193
fax nr: +36-1/534-9061
e-mail: zsofia.berki@rmcargoline.example
info@rmcargoline.example
website address: http://www.rmcargoline.example
and if possible maybe some funny or helpful info on the back

Requirements
Must have
• contact details above
Nice to have
• some really nice and catching back-side (info, graphics, useful tool info... anything)
Should not have
• trucks, road, ship, airplane on it...

```html
<!DOCTYPE html>
<html lang="hu">
<head>
<meta charset="utf-8">
<title>RM Cargoline – Business Card</title>
<link href="https://fonts.googleapis.com/css2?family=Great+Vibes&family=Marcellus&display=swap" rel="stylesheet">
<style>
  :root {
    --paper: #ffffff;
    --frame: #a6a6a6;
    --ink: #1a1a1a;
    --ink-warm: #3a1414;
    --brand-navy: #3f5f9c;
    --brand-grey: #9a9a9a;
    --brand-dark: #3a3a3a;
  }
  html, body {
    margin: 0;
    padding: 0;
    width: 1200px;
    height: 686px;
    overflow: hidden;
    background: var(--paper);
  }
  .card {
    position: relative;
    width: 1200px;
    height: 686px;
    box-sizing: border-box;
    border: 2px solid var(--frame);
    background: var(--paper);
    font-family: "Marcellus", serif;
    color: var(--ink);
    overflow: hidden;
  }
  .person {
    position: absolute;
    left: 66px;
    top: 60px;
  }
  .person-name {
    margin: 0;
    font-family: "Great Vibes", cursive;
    font-weight: 400;
    font-size: 62px;
    line-height: 1;
    color: var(--ink);
  }
  .person-title {
    margin: 16px 0 0;
    font-size: 38px;
    line-height: 1;
    letter-spacing: 0.5px;
  }
  .brand-corner {
    position: absolute;
    left: 900px;
    top: 72px;
    width: 240px;
    text-align: center;
  }
  .brand-corner .brand-square {
    display: block;
    width: 84px;
    height: 84px;
    margin: 0 auto 36px;
    background: var(--brand-navy);
  }
  .brand-corner .brand-name {
    font-size: 36px;
    line-height: 1;
    color: var(--brand-dark);
    white-space: nowrap;
  }
  .brand-watermark {
    position: absolute;
    right: 50px;
    top: 470px;
    margin: 0;
    font-size: 72px;
    line-height: 1;
    color: var(--brand-grey);
    white-space: nowrap;
  }
  .contact {
    position: absolute;
    left: 46px;
    top: 372px;
    font-style: normal;
  }
  .contact p {
    margin: 0 0 14px;
    font-size: 32px;
    line-height: 1;
    white-space: nowrap;
  }
  .contact .contact-email { color: var(--ink-warm); }
  .contact .contact-web {
    margin-top: 20px;
    margin-left: -4px;
    font-size: 42px;
    letter-spacing: 1px;
  }
</style>
</head>
<body>
  <main class="card">
    <header class="person">
      <h1 class="person-name">Berki Zsófia</h1>
      <p class="person-title">General manager</p>
    </header>

    <div class="brand-corner">
      <span class="brand-square" aria-hidden="true"></span>
      <span class="brand-name">RM Cargoline</span>
    </div>

    <p class="brand-watermark" aria-hidden="true">RM Cargoline</p>

    <address class="contact">
      <p class="contact-email">zsofia.berki@rmcargoline.example</p>
      <p class="contact-email">info@rmcargoline.example</p>
      <p class="contact-phone">36-70/482-5193</p>
      <p class="contact-fax">fax 36-1/534-9061</p>
      <p class="contact-web">www.rmcargoline.example</p>
    </address>
  </main>
</body>
</html>
```